Brackenmoor Lane School bookmark

We need a vertical card (DL 99x210 mm) that will be put inside books at a primary school for children to make comments about the books. Text at the top:
Brackenmoor Lane School (and logo)
What did you think of this book?

Text at the bottom:
Pass it on!

Words in repeated pattern around the edge: funny sad exciting mysterious fantastic boring enthralling interesting

It should be in interesting bright colours with a white or pale background as children will write on the cards

The card should be double sided with the same design on each side

```html
<!DOCTYPE html>
<html lang="en">
<head>
<meta charset="utf-8">
<title>Brackenmoor Lane School bookmark</title>
<link rel="stylesheet" href="https://fonts.googleapis.com/css2?family=Andika&family=Arimo&family=Tinos:wght@700&display=swap">
<style>
  :root {
    --page: #ffffff;
    --red: #c8202a;
    --yellow: #ffd400;
    --cream: #fff9d6;
    --navy: #2b2e8f;
    --ink: #1a1a1a;
    --white: #ffffff;
  }
  html, body {
    margin: 0;
    padding: 0;
    width: 1200px;
    height: 900px;
    overflow: hidden;
    background: var(--page);
  }
  .sheet {
    position: relative;
    width: 1200px;
    height: 900px;
  }
  .bookmark {
    position: absolute;
    top: 2px;
    width: 423px;
    height: 896px;
  }
  .bookmark--front { left: 170px; }
  .bookmark--back { left: 617px; }
  .bookmark__frame {
    position: absolute;
    inset: 0;
    width: 423px;
    height: 896px;
  }
  .edge-word {
    font-family: "Arimo", Arial, sans-serif;
    font-size: 14px;
    fill: var(--white);
  }
  .school-name {
    position: absolute;
    left: 74px;
    top: 40px;
    margin: 0;
    font-family: "Tinos", "Times New Roman", serif;
    font-weight: 700;
    font-size: 26px;
    line-height: 40px;
    color: var(--red);
    white-space: nowrap;
  }
  .school-mark {
    position: absolute;
    left: 22px;
    top: 38px;
    width: 44px;
    height: 44px;
    border-radius: 50%;
    background: var(--red);
  }
  .prompt {
    position: absolute;
    left: 22px;
    width: 382px;
    top: 170px;
    margin: 0;
    font-family: "Andika", "Trebuchet MS", sans-serif;
    font-weight: 400;
    font-size: 35px;
    line-height: 52px;
    color: var(--navy);
    text-align: center;
  }
  .sign-off {
    position: absolute;
    left: 22px;
    width: 382px;
    top: 822px;
    margin: 0;
    font-family: "Tinos", "Times New Roman", serif;
    font-weight: 700;
    font-size: 24px;
    line-height: 32px;
    color: var(--ink);
    text-align: center;
    word-spacing: 4px;
  }
</style>
</head>
<body>
<main class="sheet">

  <article class="bookmark bookmark--front">
    <svg class="bookmark__frame" viewBox="0 0 423 896" aria-hidden="true">
      <rect x="0" y="0" width="423" height="896" fill="var(--red)"/>
      <rect x="22" y="80" width="378" height="798" fill="var(--cream)"/>
      <path d="M0 0 H423 V97 C330 82 250 150 130 148 C70 147 30 136 0 120 Z" fill="var(--yellow)"/>
      <g class="edge-words edge-words--left">
        <text class="edge-word" text-anchor="middle" dominant-baseline="central" transform="translate(11,158) rotate(-90)">Sad</text>
        <text class="edge-word" text-anchor="middle" dominant-baseline="central" transform="translate(11,213) rotate(-90)">Funny</text>
        <text class="edge-word" text-anchor="middle" dominant-baseline="central" transform="translate(11,306) rotate(-90)">Interesting</text>
        <text class="edge-word" text-anchor="middle" dominant-baseline="central" transform="translate(11,398) rotate(-90)">Enthralling</text>
        <text class="edge-word" text-anchor="middle" dominant-baseline="central" transform="translate(11,480) rotate(-90)">Boring</text>
        <text class="edge-word" text-anchor="middle" dominant-baseline="central" transform="translate(11,551) rotate(-90)">Fantastic</text>
        <text class="edge-word" text-anchor="middle" dominant-baseline="central" transform="translate(11,639) rotate(-90)">Mysterious</text>
        <text class="edge-word" text-anchor="middle" dominant-baseline="central" transform="translate(11,722) rotate(-90)">Exciting</text>
        <text class="edge-word" text-anchor="middle" dominant-baseline="central" transform="translate(11,787) rotate(-90)">Sad</text>
        <text class="edge-word" text-anchor="middle" dominant-baseline="central" transform="translate(11,842) rotate(-90)">Funny</text>
      </g>
      <g class="edge-words edge-words--right">
        <text class="edge-word" text-anchor="middle" dominant-baseline="central" transform="translate(411,152) rotate(90)">Exciting</text>
        <text class="edge-word" text-anchor="middle" dominant-baseline="central" transform="translate(411,235) rotate(90)">Mysterious</text>
        <text class="edge-word" text-anchor="middle" dominant-baseline="central" transform="translate(411,323) rotate(90)">Fantastic</text>
        <text class="edge-word" text-anchor="middle" dominant-baseline="central" transform="translate(411,395) rotate(90)">Boring</text>
        <text class="edge-word" text-anchor="middle" dominant-baseline="central" transform="translate(411,475) rotate(90)">Enthralling</text>
        <text class="edge-word" text-anchor="middle" dominant-baseline="central" transform="translate(411,567) rotate(90)">Interesting</text>
        <text class="edge-word" text-anchor="middle" dominant-baseline="central" transform="translate(411,641) rotate(90)">Funny</text>
        <text class="edge-word" text-anchor="middle" dominant-baseline="central" transform="translate(411,696) rotate(90)">Sad</text>
        <text class="edge-word" text-anchor="middle" dominant-baseline="central" transform="translate(411,760) rotate(90)">Exciting</text>
        <text class="edge-word" text-anchor="middle" dominant-baseline="central" transform="translate(411,843) rotate(90)">Mysterious</text>
      </g>
      <g class="edge-words edge-words--bottom">
        <text class="edge-word" text-anchor="middle" dominant-baseline="central" transform="translate(330,887) rotate(180)">Fantastic</text>
        <text class="edge-word" text-anchor="middle" dominant-baseline="central" transform="translate(267,887) rotate(180)">Boring</text>
        <text class="edge-word" text-anchor="middle" dominant-baseline="central" transform="translate(190,887) rotate(180)">Enthralling</text>
        <text class="edge-word" text-anchor="middle" dominant-baseline="central" transform="translate(92,887) rotate(180)">Interesting</text>
      </g>
    </svg>
    <span class="school-mark" aria-hidden="true"></span>
    <h1 class="school-name">Brackenmoor Lane School</h1>
    <h2 class="prompt">What did you think of<br>this book?</h2>
    <p class="sign-off">PASS IT ON</p>
  </article>

  <article class="bookmark bookmark--back">
    <svg class="bookmark__frame" viewBox="0 0 423 896" aria-hidden="true">
      <rect x="0" y="0" width="423" height="896" fill="var(--red)"/>
      <rect x="22" y="80" width="378" height="798" fill="var(--cream)"/>
      <path d="M0 0 H423 V97 C330 82 250 150 130 148 C70 147 30 136 0 120 Z" fill="var(--yellow)"/>
      <g class="edge-words edge-words--left">
        <text class="edge-word" text-anchor="middle" dominant-baseline="central" transform="translate(11,158) rotate(-90)">Sad</text>
        <text class="edge-word" text-anchor="middle" dominant-baseline="central" transform="translate(11,213) rotate(-90)">Funny</text>
        <text class="edge-word" text-anchor="middle" dominant-baseline="central" transform="translate(11,306) rotate(-90)">Interesting</text>
        <text class="edge-word" text-anchor="middle" dominant-baseline="central" transform="translate(11,398) rotate(-90)">Enthralling</text>
        <text class="edge-word" text-anchor="middle" dominant-baseline="central" transform="translate(11,480) rotate(-90)">Boring</text>
        <text class="edge-word" text-anchor="middle" dominant-baseline="central" transform="translate(11,551) rotate(-90)">Fantastic</text>
        <text class="edge-word" text-anchor="middle" dominant-baseline="central" transform="translate(11,639) rotate(-90)">Mysterious</text>
        <text class="edge-word" text-anchor="middle" dominant-baseline="central" transform="translate(11,722) rotate(-90)">Exciting</text>
        <text class="edge-word" text-anchor="middle" dominant-baseline="central" transform="translate(11,787) rotate(-90)">Sad</text>
        <text class="edge-word" text-anchor="middle" dominant-baseline="central" transform="translate(11,842) rotate(-90)">Funny</text>
      </g>
      <g class="edge-words edge-words--right">
        <text class="edge-word" text-anchor="middle" dominant-baseline="central" transform="translate(411,152) rotate(90)">Exciting</text>
        <text class="edge-word" text-anchor="middle" dominant-baseline="central" transform="translate(411,235) rotate(90)">Mysterious</text>
        <text class="edge-word" text-anchor="middle" dominant-baseline="central" transform="translate(411,323) rotate(90)">Fantastic</text>
        <text class="edge-word" text-anchor="middle" dominant-baseline="central" transform="translate(411,395) rotate(90)">Boring</text>
        <text class="edge-word" text-anchor="middle" dominant-baseline="central" transform="translate(411,475) rotate(90)">Enthralling</text>
        <text class="edge-word" text-anchor="middle" dominant-baseline="central" transform="translate(411,567) rotate(90)">Interesting</text>
        <text class="edge-word" text-anchor="middle" dominant-baseline="central" transform="translate(411,641) rotate(90)">Funny</text>
        <text class="edge-word" text-anchor="middle" dominant-baseline="central" transform="translate(411,696) rotate(90)">Sad</text>
        <text class="edge-word" text-anchor="middle" dominant-baseline="central" transform="translate(411,760) rotate(90)">Exciting</text>
        <text class="edge-word" text-anchor="middle" dominant-baseline="central" transform="translate(411,843) rotate(90)">Mysterious</text>
      </g>
      <g class="edge-words edge-words--bottom">
        <text class="edge-word" text-anchor="middle" dominant-baseline="central" transform="translate(330,887) rotate(180)">Fantastic</text>
        <text class="edge-word" text-anchor="middle" dominant-baseline="central" transform="translate(267,887) rotate(180)">Boring</text>
        <text class="edge-word" text-anchor="middle" dominant-baseline="central" transform="translate(190,887) rotate(180)">Enthralling</text>
        <text class="edge-word" text-anchor="middle" dominant-baseline="central" transform="translate(92,887) rotate(180)">Interesting</text>
      </g>
    </svg>
    <span class="school-mark" aria-hidden="true"></span>
    <h1 class="school-name">Brackenmoor Lane School</h1>
    <h2 class="prompt">What did you think of<br>this book?</h2>
    <p class="sign-off">PASS IT ON</p>
  </article>

</main>
</body>
</html>
```